Business Card Design Project - IT Company

CLOUD IT company working with medium to large corporate clients requires 2 sided Business Card design.

Strong, Professional and modern is what I am looking for.

The Logo JPG attached has all the colour palette options. which consist of Red and Silver on various backgrounds

Preferred option for the Back of card is either Silver Text on Red or Silver Text on Black. Though this is not concrete. Surprise me.

Logo must be prominent along with Contact details of the staff member

Tagline can be all Capitals " CLOUD MANAGED SERVICES"

I will look to provide feedback and tweaks to get the right design so it should be a fun process.

I will provide the layered files to the top few contenders.

Reason: Leaving the door open for some creativity. Don't forget this is an technology company. .

Target Market(s)

Leaders, decision makers, CEOs, CIOs,

Industry/Entity Type

Business

Requirements
Must have
• Data must have is

Company Name: Brelquist
Tagline: Cloud Managed Services

No Particular order

First Name Last name
Director
Mobile 0477 555 019
www.brelquist-example.com
First.Lastname@brelquist-example.com
Suite 7, 48 Wexmoor Lane, Sydney NSW 2000

```html
<!DOCTYPE html>
<html lang="en">
<head>
<meta charset="utf-8">
<title>Brelquist – Business Card</title>
<link rel="stylesheet" href="https://fonts.googleapis.com/css2?family=Fira+Sans:wght@400;500;600;700&display=swap">
<style>
  :root {
    --stage: #1c1c1e;
    --red: #a51f24;
    --black: #0d0d0d;
    --grey: #5f6062;
    --silver: #d9dadc;
    --ink: #1a1a1a;
    --paper: #ffffff;
    --faint: #ececed;
  }
  * { box-sizing: border-box; margin: 0; padding: 0; }
  html, body { width: 1200px; height: 900px; overflow: hidden; }
  body {
    background: var(--stage);
    font-family: "Fira Sans", Arial, sans-serif;
    position: relative;
  }
  .card {
    position: absolute;
    top: 307px;
    width: 500px;
    height: 286px;
    overflow: hidden;
    box-shadow: 0 10px 30px rgba(0,0,0,.55);
  }

  /* Back of card */
  .card-back { left: 70px; background: var(--grey); }
  .back-top { position: absolute; left: 0; top: 0; width: 100%; height: 62px; background: var(--black); }
  .back-band {
    position: absolute; left: 0; top: 62px; width: 100%; height: 128px;
    background: var(--red);
    border-top: 3px solid var(--silver);
    border-bottom: 3px solid var(--silver);
    display: flex; align-items: center; justify-content: center;
  }
  .back-logo { display: flex; align-items: center; gap: 14px; }
  .logo-dot { width: 34px; height: 34px; border-radius: 50%; background: var(--silver); flex: none; }
  .back-wordmark { display: flex; flex-direction: column; align-items: flex-end; }
  .back-name { color: var(--silver); font-weight: 700; font-size: 52px; line-height: 1; letter-spacing: -0.5px; }
  .back-tagline { color: var(--silver); font-weight: 600; font-size: 11px; letter-spacing: 0.8px; margin-top: 3px; }
  .back-url {
    position: absolute; left: 0; top: 190px; width: 100%; height: 96px;
    display: flex; align-items: center; justify-content: center;
    color: var(--silver); font-size: 14px; letter-spacing: 4px;
  }

  /* Front of card */
  .card-front { left: 630px; background: var(--paper); }
  .front-watermark {
    position: absolute; right: -70px; top: 70px;
    width: 230px; height: 230px; border-radius: 50%;
    background: var(--faint);
  }
  .front-logo { position: absolute; left: 30px; top: 28px; display: flex; align-items: center; gap: 10px; }
  .front-logo .logo-dot { width: 26px; height: 26px; background: var(--red); }
  .front-wordmark { display: flex; flex-direction: column; align-items: flex-end; }
  .front-name { color: var(--ink); font-weight: 700; font-size: 36px; line-height: 1; }
  .front-tagline { color: var(--ink); font-weight: 600; font-size: 8px; letter-spacing: 0.6px; margin-top: 2px; }
  .staff { position: absolute; left: 30px; top: 104px; }
  .staff-name { color: var(--red); font-weight: 500; font-size: 15px; letter-spacing: 0.5px; text-transform: uppercase; }
  .staff-role { color: var(--ink); font-size: 11px; margin-top: 1px; }
  .contact { position: absolute; left: 30px; top: 156px; color: var(--ink); font-size: 11.5px; line-height: 1.6; }
  .contact .accent { color: var(--red); }
  .front-bar { position: absolute; left: 0; bottom: 0; width: 100%; height: 14px; display: flex; }
  .front-bar .bar-red { width: 62%; background: var(--red); }
  .front-bar .bar-grey { flex: 1; background: var(--grey); }
</style>
</head>
<body>
  <section class="card card-back" aria-label="Business card back">
    <div class="back-top"></div>
    <div class="back-band">
      <div class="back-logo">
        <span class="logo-dot"></span>
        <div class="back-wordmark">
          <span class="back-name">Brelquist</span>
          <span class="back-tagline">CLOUD MANAGED SERVICES</span>
        </div>
      </div>
    </div>
    <div class="back-url">WWW.BRELQUIST-EXAMPLE.COM</div>
  </section>

  <section class="card card-front" aria-label="Business card front">
    <div class="front-watermark"></div>
    <div class="front-logo">
      <span class="logo-dot"></span>
      <div class="front-wordmark">
        <span class="front-name">Brelquist</span>
        <span class="front-tagline">CLOUD MANAGED SERVICES</span>
      </div>
    </div>
    <div class="staff">
      <p class="staff-name">Marla Venhoek</p>
      <p class="staff-role">Director</p>
    </div>
    <div class="contact">
      <p>M: 0477 555 019</p>
      <p><span class="accent">mvenhoek</span>@brelquist-example.com | www.<span class="accent">brelquist-example</span>.com</p>
      <p>Suite 7, 48 Wexmoor Lane, Sydney NSW 2000</p>
    </div>
    <div class="front-bar"><span class="bar-red"></span><span class="bar-grey"></span></div>
  </section>
</body>
</html>
```